Veteran Owned General Contractor needs Bold New Business Cards

We are a service disabled veteran owned small business. We're a general contractor that specializes in excavation, underground utilities, site work, land clearing and demolition. We would like a fresh, simple, bold, new look for our business cards. We're open to ideas! We'd like to incorporate the following information on the card:

Company Name & Logo, Name of Person, Job Title, Office Phone, Fax, Cell Phone, Email Address, Website, SDVOSB

Our logo is included. We look forward to your thoughts.

Thank you!
Updates

Reason: Hello Due to the overwhelming response to this project, we are extending the deadline one time to allow for improved communication and feedback with the top candidates. We would like to thank everyone for their hard work and exceptional creativity! Thank you

Industry/Entity Type

Business

Contact Information for Business Card

Font styles to use
Sans Serif

Requirements
Nice to have
• As we are a veteran owned company, it would be nice to incorporate an American flag into the design. Maybe on the back?

```html
<!DOCTYPE html>
<html lang="en">
<head>
<meta charset="utf-8">
<title>Stonefield Business Cards</title>
<link rel="stylesheet" href="https://fonts.googleapis.com/css2?family=Montserrat:wght@800&family=Open+Sans:wght@400;700&display=swap">
<style>
  :root {
    --backdrop-top: #161616;
    --backdrop-bottom: #303030;
    --card-white: #fbfbfb;
    --card-grey: #ececec;
    --brand-green: #6cbd45;
    --text-grey: #6e6e6e;
    --rule-grey: #8a8a8a;
    --flag-navy: #1f2f6e;
    --flag-red: #c0173d;
  }
  * { margin: 0; padding: 0; box-sizing: border-box; }
  html, body { width: 1200px; height: 900px; overflow: hidden; }
  body {
    position: relative;
    background: linear-gradient(to bottom, var(--backdrop-top), var(--backdrop-bottom));
    font-family: "Open Sans", Arial, sans-serif;
  }
  .card {
    position: absolute;
    top: 170px;
    width: 347px;
    height: 561px;
    box-shadow: 0 2px 6px rgba(0,0,0,.45);
  }
  .card--front { left: 259px; background: var(--card-white); }
  .card--back {
    left: 631px;
    background: linear-gradient(to bottom, var(--card-grey), #f7f7f7 45%, #ffffff);
    overflow: hidden;
  }

  /* front */
  .brand-lockup {
    position: absolute;
    top: 80px; left: 0; width: 100%;
    height: 170px;
    display: flex; align-items: center; justify-content: center; gap: 12px;
  }
  .brand-square { width: 30px; height: 30px; background: var(--brand-green); }
  .brand-name {
    font-family: "Montserrat", Arial, sans-serif;
    font-weight: 800;
    font-size: 34px;
    letter-spacing: 1px;
    color: var(--brand-green);
  }
  .person {
    position: absolute; top: 322px; left: 0; width: 100%;
    text-align: center;
  }
  .person-name {
    font-family: "Montserrat", Arial, sans-serif;
    font-weight: 800;
    font-size: 23px;
    color: var(--brand-green);
    line-height: 30px;
  }
  .person-title { font-size: 15px; color: var(--text-grey); line-height: 20px; }
  .divider {
    position: absolute; top: 384px; left: 86px;
    width: 175px; height: 2px; background: var(--rule-grey);
  }
  .contact-list {
    position: absolute; top: 407px; left: 0; width: 100%;
    list-style: none; text-align: center;
    font-size: 15px; line-height: 20px; color: var(--text-grey);
  }
  .contact-label { color: var(--brand-green); font-weight: 700; }
  .contact-web { color: var(--brand-green); font-weight: 700; }

  /* back */
  .back-lockup {
    position: absolute; top: 48px; left: 0; width: 100%;
    display: flex; flex-direction: column; align-items: center; gap: 18px;
  }
  .back-lockup .brand-square { width: 56px; height: 56px; }
  .back-lockup .brand-name { font-size: 36px; }
  .flag-art {
    position: absolute; top: 268px; left: 0;
    width: 347px; height: 282px;
    background: linear-gradient(160deg, var(--flag-navy) 0%, var(--flag-navy) 30%, #6b2455 55%, var(--flag-red) 80%, var(--flag-red) 100%);
  }
</style>
</head>
<body>
  <section class="card card--front">
    <div class="brand-lockup">
      <span class="brand-square"></span>
      <span class="brand-name">STONEFIELD</span>
    </div>
    <div class="person">
      <p class="person-name">DANIEL REEVES</p>
      <p class="person-title">Managing Director</p>
    </div>
    <div class="divider"></div>
    <ul class="contact-list">
      <li><span class="contact-label">P:</span> 555-010 234 567</li>
      <li><span class="contact-label">M:</span> 555-010 234 567</li>
      <li><span class="contact-label">F:</span> 555-010 234 567</li>
      <li><span class="contact-label">E:</span> info@stonefieldco.com</li>
      <li class="contact-web">www.stonefieldco.com</li>
    </ul>
  </section>

  <section class="card card--back">
    <div class="back-lockup">
      <span class="brand-square"></span>
      <span class="brand-name">STONEFIELD</span>
    </div>
    <div class="flag-art" role="img" aria-label="Paint-splash illustration of the American flag with white stars on navy and red and white stripes"></div>
  </section>
</body>
</html>
```